Web Design Project Bright Lane

I am needing a website for a theatre called Bright Lane Stage School (blstageschool.com) which has already been purchsed from web nook. (Let me know if you need any other info on that.)We need a website that is professional looking and easy to access. Attached is the logo as well as the business card design. I think it would be nice to have the same type of design that’s on the business card but I am definitely open to other creative ideas. I need the website to be in a format where I can edit it in the future when I need to add classes and events to it. Also, some other things I need are I need are a…
A homepage. On the homepage we would like the motto, “Rise to the spotlight.” Also, the mission statement,
Bright Lane Stage School strives to help students achieve excellence in performance, while building self-confidence and creativity. The Bright Lane Stage School has created a fun and safe environment, where students can learn, acquire new skills, and explore their potential through musical theatre. Students not only have the freedom to, but are encouraged to embrace who they are and can lose their fear of judgment from others.
Class Registration Page for the classes- (As well as a quick fund option for each if that is possible)
4-6 Musical Theatre
Tuesday’s 4:00PM-5:00PM
January 6th – February 24th
8 Weeks
Cost $160
Curriculum: Moss Kite
Class info: In MT 4-6 your students will learn the basics of singing, dancing, and acting. A lesson of theatre terminology or technique will be taught each week as well as working on the show that will be performed at the end of the 8 weeks semester.

6-9 Musical Theatre
Tuesday’s 5:15PM-6:45PM
January 6th- February 24th
8 Weeks
Cost: $200
Curriculum: Delia
Class info: In MT 6-9 your students will learn the basics of singing, dancing, and acting. A lesson of theatre terminology or technique will be taught each week as well as working on the show that will be performed at the end of the 8 weeks semester.
9-12 Musical Theatre
Wednesday’s 5:00-7:00PM
8 Weeks
Cost: $240
Curriculum: Gilded
Class info: In MT 9-12 your students will learn intermediate levels of singing, dancing, and acting. A lesson of theatre terminology or technique will be taught each week as well as working on the show that will be performed at the end of the 8 weeks semester.

About- (Include headshot that is attached)
A native Coloradan, Marisol is an actress, director, teacher, and wife. She was a Dean’s List graduate of Northvale College in Florida, she holds a B.S. degree in Theatre. Her Capstone Project involved writing, producing, directing, and starring in a 60-minute one-woman musical which was noted by the Chairman of Theatre as setting new standard for the NVC project. Initially attending Harrow Ridge College, Marisol was one of nine students representing HR at the Upper Plains Drama Festival. Marisol has also been a senior theatre director at the Willowmere Youth Playhouse for 4 years, where she directed fall, spring, and summer classes for ages 4-19. Her experience includes directing the main stage production, Quill Tr., assistant director for, Nobody Minds Old Tobias Grey, and stage management for Der Wandelstern.

Contact us
Phone: 555-214-7390
Email: blstageschoolhub.com

Also, I do not have any photos of students yet so it's ok if their aren't many pictures because I intend on adding some when things get going, so if it's simple that's great. Also, if you find any musical theatre pictures that don't include faces, are just bodies or feet, that would work as well.
Updates

The web address needs to be blstageschool.com. I have already purchased the domain name from WebNook. Let me know if there are any steps I might be missing or any other info I need to provide. Also, I need to be able to edit the website in the future but I'm not sure which format is best for that.

Target Market(s)

Theatre parents and students

Industry/Entity Type

Building

Requirements
Must have
• Stated above.

```html
<!DOCTYPE html>
<html lang="en">
<head>
<meta charset="utf-8">
<title>Bright Lane Stage School</title>
<link href="https://fonts.googleapis.com/css2?family=Titillium+Web:ital,wght@0,400;0,600;0,700;1,400&family=Dancing+Script:wght@600&display=swap" rel="stylesheet">
<style>
:root{
  --red:#8e0b0b;
  --ink:#111;
  --text:#555;
  --panel:#e4e4e4;
  --rule:#d6d6d6;
  --white:#fff;
  --stage-warm:#8a6a44;
  --stage-deep:#3a1c12;
  --drape:#9c1414;
}
*{box-sizing:border-box;margin:0;padding:0}
html,body{width:1084px;height:1200px;overflow:hidden;background:var(--white)}
body{position:relative;font-family:"Titillium Web",sans-serif;color:var(--text)}
.top-rule{position:absolute;left:0;top:0;width:1084px;height:5px;background:var(--red)}
.brand{position:absolute;left:90px;top:40px;display:flex;align-items:center;gap:10px}
.brand-mark{width:18px;height:18px;background:var(--red)}
.brand-name{font-size:28px;font-weight:600;color:var(--red);line-height:1}
.quick-contact{position:absolute;right:90px;top:36px;text-align:right;line-height:1.15}
.quick-contact .label{font-size:22px;color:var(--ink)}
.quick-contact .phone{font-size:22px;color:var(--red)}
.main-nav{position:absolute;left:90px;top:116px;width:904px;height:63px;background:var(--red);border-radius:6px}
.main-nav a{position:absolute;top:21px;color:var(--white);font-size:13px;font-weight:600;text-decoration:none}
.slider{position:absolute;left:90px;top:195px;width:904px;height:428px;border:1px solid var(--rule);border-radius:6px;background:var(--white);box-shadow:0 8px 8px -6px rgba(0,0,0,.18)}
.slide-image{position:absolute;left:5px;top:5px;width:892px;height:416px;background:linear-gradient(90deg,var(--drape) 0%,var(--stage-deep) 18%,var(--stage-warm) 50%,var(--stage-deep) 82%,var(--drape) 100%)}
.motto{position:absolute;left:0;top:180px;width:892px;text-align:center;font-family:"Dancing Script",cursive;font-size:44px;color:var(--white)}
.slide-arrow{position:absolute;top:195px}
.dots{position:absolute;left:5px;top:380px;width:892px}
.welcome{position:absolute;left:90px;top:651px;font-size:27px;font-weight:400;color:var(--ink)}
.welcome span{color:var(--red)}
.portrait{position:absolute;left:89px;top:706px;width:166px;height:210px;border:1px solid var(--rule);padding:3px;background:var(--white)}
.portrait div{width:100%;height:100%;background:linear-gradient(160deg,#d8d8d8,#8a8a8a 55%,#c4c4c4)}
.mission{position:absolute;left:267px;top:712px;width:440px;font-size:12.3px;line-height:21.7px}
.class-card{position:absolute;left:733px;top:649px;width:261px;height:276px;background:var(--panel);border:1px solid #cfcfcf}
.class-card header{height:41px;background:var(--red);color:var(--white);font-size:16px;padding:9px 12px}
.class-card .arrows{position:absolute;right:12px;top:12px}
.class-card .body{padding:6px 18px 0 12px;font-size:10.5px;line-height:21.7px;color:#333}
.class-card .key{color:var(--red);font-weight:600}
.scroll-track{position:absolute;right:0;top:41px;width:9px;height:234px;background:#8a8a8a}
.scroll-thumb{position:absolute;right:0;top:52px;width:9px;height:33px;background:var(--red)}
.section-title{position:absolute;left:91px;top:952px;font-size:27px;color:var(--red);font-weight:400}
.quote{position:absolute;top:1008px;width:440px}
.quote p{padding-left:17px;padding-right:30px;font-size:12px;line-height:21.7px}
.quote cite{display:block;text-align:right;padding-right:30px;font-size:11px;color:var(--ink);margin-top:2px}
.qmark{position:absolute;font-family:Georgia,serif;font-size:34px;color:#999;line-height:1}
.site-footer{position:absolute;left:0;top:1107px;width:1084px;height:93px;background:var(--red);color:var(--white)}
.footer-links{position:absolute;left:90px;top:26px;font-size:11.5px}
.footer-links a{color:var(--white);text-decoration:none}
.copyright{position:absolute;left:90px;top:48px;font-size:11.5px}
.social{position:absolute;left:884px;top:39px;display:flex;gap:8px}
.social span{width:21px;height:21px;border-radius:3px;background:#4d6fa8}
</style>
</head>
<body>
<div class="top-rule"></div>

<div class="brand"><span class="brand-mark"></span><span class="brand-name">Bright Lane</span></div>

<div class="quick-contact"><div class="label">Quick contact</div><div class="phone">555-214-7390</div></div>

<nav class="main-nav">
  <a style="left:46px">Home</a>
  <a style="left:159px">About Us</a>
  <a style="left:290px">Services</a>
  <a style="left:417px">Testimonals</a>
  <a style="left:564px">Bio</a>
  <a style="left:662px">Blog</a>
  <a style="left:768px">Contact Us</a>
</nav>

<section class="slider">
  <div class="slide-image" role="img" aria-label="Photo of a theatre stage framed by red curtains and a gilded proscenium">
    <div class="motto">Rise to the spotlight.</div>
  </div>
  <svg class="slide-arrow" style="left:24px" width="30" height="30" viewBox="0 0 30 30"><circle cx="15" cy="15" r="14" fill="#f2f2f2" stroke="#ccc"/><path d="M17 9l-6 6 6 6" fill="none" stroke="#333" stroke-width="2.5"/></svg>
  <svg class="slide-arrow" style="left:848px" width="30" height="30" viewBox="0 0 30 30"><circle cx="15" cy="15" r="14" fill="#f2f2f2" stroke="#ccc"/><path d="M13 9l6 6-6 6" fill="none" stroke="#333" stroke-width="2.5"/></svg>
  <svg class="dots" height="14" viewBox="0 0 892 14"><circle cx="422" cy="7" r="5.5" fill="#a00" stroke="#fff" stroke-width="1.5"/><circle cx="441" cy="7" r="5.5" fill="#eee"/><circle cx="460" cy="7" r="5.5" fill="#eee"/></svg>
</section>

<h1 class="welcome">Welcome To <span>Bright Lane</span></h1>
<div class="portrait"><div role="img" aria-label="Black and white headshot of the school's director"></div></div>
<p class="mission">Bright Lane Stage School strives to help students achieve excellence in performance, while building self-confidence and creativity. The Bright Lane Stage School has created a fun and safe environment, where students can learn, acquire new skills, and explore their potential through musical theatre. Students not only have the freedom to, but are encouraged to embrace who they are and can lose their fear of judgment from others.<br>Classes attached too. You can find a nice way to display that too and when clicked takes to detailed page and shows fill info or on mouse over shows informations or course details.</p>

<aside class="class-card">
  <header>46 Musical Theatre</header>
  <svg class="arrows" width="24" height="14" viewBox="0 0 24 14"><path d="M8 1L2 7l6 6M16 1l6 6-6 6" fill="none" stroke="#fff" stroke-width="2.5"/></svg>
  <div class="body">
    Tuesday's 4:00PM5:00PM<br>January 6th – February 24th<br>8 Weeks<br>Cost $160<br>
    <span class="key">Curriculum:</span> Moss Kite<br>
    <span class="key">Class info:</span> In MT 46 your students will learn the basics of singing, dancing, and acting. A lesson of theatre terminology or technique will be taught each week as well as working on the show that will be performed at the end of the 8 weeks semester.
  </div>
  <div class="scroll-track"></div><div class="scroll-thumb"></div>
</aside>

<h2 class="section-title">Testimonials</h2>
<div class="quote" style="left:90px">
  <span class="qmark" style="left:0;top:-10px">“</span>
  <p>Lorem ipsum dolor sit amet, consectetuer adipiscing elit. Aenean commodo ligula eget dolor. Aenean massa. Cum sociis natoque penatibus et</p>
  <cite>-Ravi Solenko, CEO</cite>
  <span class="qmark" style="left:422px;top:42px">”</span>
</div>
<div class="quote" style="left:554px">
  <span class="qmark" style="left:0;top:-10px">“</span>
  <p>Lorem ipsum dolor sit amet, consectetuer adipiscing elit. Aenean commodo ligula eget dolor. Aenean massa. Cum sociis natoque penatibus et</p>
  <cite>-Ravi Solenko, CEO</cite>
  <span class="qmark" style="left:422px;top:42px">”</span>
</div>

<footer class="site-footer">
  <div class="footer-links"><a>Home</a> &nbsp;|&nbsp; <a>About Us</a> &nbsp;|&nbsp; <a>Products</a> &nbsp;|&nbsp; <a>Contact Us</a></div>
  <div class="copyright">© 2014 Company Name &nbsp;All right reserved &nbsp;Term of Use</div>
  <div class="social"><span></span><span style="background:#4fb3e3"></span><span style="background:#2a6fb0"></span><span style="background:#f08a1c"></span></div>
</footer>
</body>
</html>
```